Chimney Service company needs new business card design

We need a updated business card with our new logo added. We provide a full range of chimney services throughout Vermont and New Hampshire. The business card will be one sided and color. Attached is our current business card another document showing all the information we would like on the card.
We dont like a lot of flashy colors.... here is a link to our website to get an idea of our branding www.flueguardnorthvt-example.com

Target Market(s)

homeowners

Industry/Entity Type

Business

Contact Information for Business Card

See attached sheet for content.

Font styles to use
Serif
Sans Serif

Requirements
Must have
• all information provided on separate sheet
Should not have
• Additional information that may clogg up design

```html
<!DOCTYPE html>
<html lang="en">
<head>
<meta charset="utf-8">
<title>Flue Guard North – Business Card</title>
<link rel="stylesheet" href="https://fonts.googleapis.com/css2?family=Open+Sans:wght@400;600&family=Russo+One&display=swap">
<style>
  :root {
    --page: #e4e4e4;
    --charcoal: #2e2e2e;
    --charcoal-deep: #262626;
    --paper: #f4f4f4;
    --paper-shade: #e6e6e6;
    --ink: #2b2b2b;
    --red: #8f0d0d;
    --red-bright: #c0211b;
    --white: #ffffff;
  }
  * { box-sizing: border-box; margin: 0; padding: 0; }
  html, body { width: 1200px; height: 576px; overflow: hidden; background: var(--page); }
  .stage { position: relative; width: 1200px; height: 576px; }

  .card {
    position: absolute;
    top: 138px;
    width: 484px;
    height: 294px;
    border-radius: 14px;
    overflow: hidden;
  }
  .card--front { left: 82px; background: var(--charcoal); }
  .card--back {
    left: 602px;
    background: linear-gradient(135deg, var(--white) 0%, var(--paper) 55%, var(--paper-shade) 100%);
  }

  /* Company name, set in the card's own sans text face */
  .brand-name {
    position: absolute;
    font-family: "Open Sans", sans-serif;
    font-weight: 600;
    letter-spacing: 1px;
    white-space: nowrap;
    text-align: center;
  }
  .card--front .brand-name {
    left: 0; right: 0; top: 132px;
    font-size: 24px;
    color: var(--white);
  }
  .card--back .brand-name {
    left: 270px; width: 200px; top: 92px;
    font-size: 17px;
    color: var(--ink);
  }

  /* Services list */
  .services {
    position: absolute;
    left: 27px; top: 32px;
    list-style: none;
    font-family: "Open Sans", sans-serif;
    font-size: 12.5px;
    color: var(--ink);
    line-height: 16.5px;
  }
  .services li { display: flex; align-items: center; gap: 8px; }
  .services svg { width: 8px; height: 11px; flex: none; }

  /* Contact */
  .contact {
    position: absolute;
    left: 26px; top: 196px;
    list-style: none;
    font-family: "Open Sans", sans-serif;
    font-size: 12.5px;
    color: var(--ink);
    line-height: 19.5px;
  }
  .contact li { display: flex; align-items: center; gap: 10px; }
  .contact svg { width: 11px; height: 11px; flex: none; }
  .contact .highlight { color: var(--red); }

  /* Service area */
  .area {
    position: absolute;
    right: 24px; top: 184px;
    text-align: right;
    font-family: "Russo One", sans-serif;
    font-size: 18.5px;
    line-height: 21px;
    color: var(--ink);
  }
  .area__since {
    display: flex;
    align-items: center;
    justify-content: flex-end;
    gap: 8px;
    margin-top: 4px;
    font-family: "Open Sans", sans-serif;
    font-size: 9.5px;
    line-height: 12px;
  }
  .area__since::before, .area__since::after {
    content: "";
    width: 58px; height: 2px;
    background: var(--red);
  }

  /* Footer bands */
  .footer { position: absolute; left: 0; bottom: 0; width: 484px; height: 40px; }
  .footer svg { position: absolute; inset: 0; }
  .footer__left, .footer__right {
    position: absolute;
    font-family: "Open Sans", sans-serif;
    font-size: 12px;
    color: var(--white);
  }
  .footer__left { left: 23px; bottom: 5px; }
  .footer__right { left: 280px; width: 190px; text-align: center; bottom: 8px; }
</style>
</head>
<body>
<main class="stage">

  <section class="card card--front" aria-label="Card front">
    <span class="brand-name">Flue Guard North</span>
  </section>

  <section class="card card--back" aria-label="Card back">
    <svg width="0" height="0" style="position:absolute">
      <defs>
        <symbol id="flame" viewBox="0 0 8 11">
          <path d="M4 0 C5 3 8 4 7 8 C6.5 10 5 11 4 11 C2 11 0.5 9.5 1 7.5 C1.3 6 2.5 5.5 2.5 4 C3.5 5 3.5 6 3.3 7 C4.5 5.5 4.8 3 4 0 Z" fill="var(--red-bright)"/>
        </symbol>
      </defs>
    </svg>

    <ul class="services">
      <li><svg><use href="#flame"/></svg>Full Masonry Services</li>
      <li><svg><use href="#flame"/></svg>Historic chimney restoration</li>
      <li><svg><use href="#flame"/></svg>Stainless steel liners</li>
      <li><svg><use href="#flame"/></svg>New Chimney installations</li>
      <li><svg><use href="#flame"/></svg>HSCA Certified Chimney sweeps</li>
    </ul>

    <span class="brand-name">Flue Guard North</span>

    <ul class="contact">
      <li>
        <svg viewBox="0 0 11 11" aria-hidden="true"><path d="M1 4 C1 2 3 1.5 5.5 1.5 C8 1.5 10 2 10 4 L8 4.5 L7.5 3.5 L3.5 3.5 L3 4.5 Z M2.5 5.5 L8.5 5.5 L9.5 9.5 L1.5 9.5 Z" fill="var(--red)"/></svg>
        802-555-0147
      </li>
      <li>
        <svg viewBox="0 0 11 11" aria-hidden="true"><rect x="0.5" y="2" width="10" height="7" fill="var(--red)"/><path d="M0.5 2 L5.5 6 L10.5 2" stroke="var(--white)" stroke-width="1" fill="none"/></svg>
        info@flueguardnorthvt-example.com
      </li>
      <li>
        <svg viewBox="0 0 11 11" aria-hidden="true"><circle cx="5.5" cy="5.5" r="4.5" fill="none" stroke="var(--red)" stroke-width="1.2"/><path d="M1 5.5 H10 M5.5 1 C3 3.5 3 7.5 5.5 10 M5.5 1 C8 3.5 8 7.5 5.5 10" stroke="var(--red)" stroke-width="1" fill="none"/></svg>
        <span>www.<span class="highlight">flueguardnorthvt-example</span>.com</span>
      </li>
    </ul>

    <div class="area">
      SERVING VT AND<br>NEW HAMPSHIRE
      <div class="area__since">SINCE 1989</div>
    </div>

    <div class="footer">
      <svg viewBox="0 0 484 40" preserveAspectRatio="none" aria-hidden="true">
        <polygon points="0,14 268,14 250,40 0,40" fill="var(--red)"/>
        <polygon points="270,0 484,0 484,40 245,40" fill="var(--charcoal-deep)"/>
      </svg>
      <span class="footer__left">Family Owned &amp; Operated</span>
      <span class="footer__right">Fully Insured – Free Estimates</span>
    </div>
  </section>

</main>
</body>
</html>
```